Halvern Dental website redesign

We need a redesign for a website: myhalverndental.com.

I already created a video going over what exactly is needed in the design.

See Video here: https://files.quorvane.com/file/d/8xKpQ2mWn4TzLrV7bHsYcE3jFuGaD6oN1/view?usp=sharing

Searchly Slide shown in Video: https://slides.quorvane.com/presentation/d/7RtW2yQnXbVc4LmPz9KsHdJf3GaE8oUi6TeYqNvB5wZx/edit?usp=sharing
Updates

Holidays in India so we did not get enough design entries or quality.

Target Market(s)

Dentistry

Industry/Entity Type

Dentistry

Number of Pages Required

1 page

Colors
0094D4
00A9DD
6FCCEA
C7EBF8
E9F6FB
00AB8E
00BBA5
67D7C9
C6EFE9
E9F9F6

Requirements
Must have
• See 13 min video link in description - shows what to do.

```html
<!DOCTYPE html>
<html lang="en">
<head>
<meta charset="utf-8">
<title>Halvern Dental</title>
<link href="https://fonts.googleapis.com/css2?family=Rubik:wght@400;500;600&family=Poppins:wght@400;500;600&display=swap" rel="stylesheet">
<style>
:root{
  --ink:#2f5468;
  --text:#5a6670;
  --green:#6cb33f;
  --red:#d7262d;
  --blue:#0098d7;
  --blue-2:#00a9dd;
  --blue-soft:#c7ebf8;
  --blue-pale:#e9f6fb;
  --grey-bg:#f3f4f6;
  --pink:#e88a8a;
}
*{box-sizing:border-box;margin:0;padding:0}
html,body{width:1200px;height:3940px;overflow:hidden;background:#fff}
body{position:relative;font-family:'Poppins',sans-serif;color:var(--text)}
.abs{position:absolute}
h1,h2,h3{font-family:'Rubik',sans-serif;color:var(--ink);font-weight:500}

.logo{left:89px;top:24px;font-family:'Rubik',sans-serif;font-size:34px;font-weight:500;color:var(--green)}
.phone{left:112px;top:96px;font-family:'Rubik',sans-serif;font-size:20px;font-weight:500;color:var(--ink)}
.locations{left:520px;top:0;width:170px;height:58px;background:var(--ink);border-radius:0 0 60px 60px;color:#fff;font-size:11px;font-weight:600;text-align:center;padding-top:12px}
.top-btn{top:45px;height:32px;border-radius:16px;color:#fff;font-size:11px;font-weight:600;text-align:center;line-height:32px}
.nav{left:320px;top:100px;display:flex;gap:28px;font-size:11px;font-weight:500;color:var(--ink);text-transform:uppercase}

.hero-bg{left:0;top:0;width:1200px;height:820px}
.hero-title{left:86px;top:272px;font-size:59px;line-height:64px;font-weight:600}
.hero-sub{left:88px;top:410px;font-size:17px;color:var(--ink);font-family:'Rubik',sans-serif}
.btn-green{background:var(--green);color:#fff;font-size:11px;font-weight:600;border-radius:22px;text-align:center;text-transform:uppercase}
.hero-art{left:640px;top:196px;width:510px;height:520px;border-radius:50%;background:radial-gradient(circle at 55% 45%,#e3f2fb 0 30%,var(--blue-2) 31% 62%,rgba(0,169,221,0) 63%)}

.section-title{width:1200px;text-align:center;font-size:44px}

.member{top:979px;width:256px;height:296px;border-radius:6px;overflow:hidden}
.member .name{position:absolute;left:38px;bottom:24px;color:#fff;font-family:'Rubik',sans-serif}
.arrow{width:40px;height:40px;border-radius:50%;background:#fff;box-shadow:0 2px 8px rgba(0,0,0,.15);display:flex;align-items:center;justify-content:center}
.btn-outline{border:1.5px solid #aab3ba;border-radius:20px;text-align:center;font-size:11px;font-weight:600;color:var(--ink)}

.service{top:1495px;width:160px;height:191px;background:#fff;border-radius:6px;box-shadow:0 4px 14px rgba(0,0,0,.08);text-align:center;font-family:'Rubik',sans-serif;font-size:17px;color:var(--ink)}
.service svg{margin-top:40px}
.service.active{background:var(--green);color:#fff}
.service p{margin-top:14px;line-height:19px}

.review-band{left:0;top:1815px;width:1200px;height:590px}
.widget{left:658px;top:1833px;width:370px;height:508px;background:#fff;border-radius:18px;box-shadow:0 6px 20px rgba(0,0,0,.1)}
.review-card{left:50px;top:204px;width:270px;height:264px;background:#f4f5f6;border-radius:8px}

.about-text{left:603px;top:2696px;width:490px;font-size:13.3px;line-height:19.6px}
.about-text p{margin-bottom:12px}

.cta{left:89px;top:3182px;width:1022px;height:338px;border-radius:16px;background:linear-gradient(120deg,#4a7389,#2f5468);overflow:hidden;text-align:center;color:#fff}

.foot-head{top:3610px;font-size:14px;font-weight:600;color:var(--ink)}
.foot-line{font-size:12px;color:var(--text)}
.hours{left:875px;top:3646px;font-size:12px;line-height:22.5px;display:grid;grid-template-columns:96px 80px}
.social{width:24px;height:24px;border-radius:50%}
</style>
</head>
<body>

<div class="abs logo">Halvern Dental</div>
<div class="abs phone">(555) 214-7730</div>
<div class="abs locations">VIEW LOCATIONS</div>
<div class="abs top-btn" style="left:849px;width:150px;background:var(--green)">SCHEDULE ONLINE</div>
<div class="abs top-btn" style="left:1006px;width:105px;background:var(--red)">EMERGENCY</div>
<nav class="abs nav">
  <span>About Us ⌄</span><span>Services ⌄</span><span>Financing</span><span>Testimonials</span><span>New Patient Visit</span><span>Specials</span><span>Contact Us</span><span>Blog</span>
</nav>

<svg class="abs hero-bg" viewBox="0 0 1200 820" aria-hidden="true">
  <defs><linearGradient id="heroGrad" x1="0" y1="0" x2="0" y2="1"><stop offset="0" stop-color="#fff"/><stop offset="1" stop-color="#eef0f3"/></linearGradient></defs>
  <path d="M0 140 H1200 V720 C1080 800 880 830 740 790 C620 755 520 620 360 610 C220 600 80 650 0 700 Z" fill="url(#heroGrad)"/>
</svg>
<div class="abs hero-art" role="img" aria-label="Illustration of teeth inside a blue swirl with sparkles"></div>
<h1 class="abs hero-title">Creating<br>Healthier Smiles</h1>
<div class="abs hero-sub">With Advanced Technology and Affordable Treatment</div>
<div class="abs btn-green" style="left:88px;top:448px;width:200px;height:43px;line-height:43px">Book an Appointment</div>

<h2 class="abs section-title" style="top:892px">Meet Our Team</h2>
<div class="abs member" style="left:203px;background:linear-gradient(160deg,#6c665d,#3c3731)" role="img" aria-label="Portrait of a dentist in a white coat"></div>
<div class="abs member" style="left:473px;background:linear-gradient(160deg,#4f6c7c,#2f4a58)" role="img" aria-label="Portrait of Dr. Anika Varma">
  <div class="name"><div style="font-size:17px;font-weight:500">Dr. Anika Varma</div><div style="font-size:12px">Endodontist<br>DDS</div></div>
</div>
<div class="abs member" style="left:741px;background:linear-gradient(160deg,#777066,#4a443d)" role="img" aria-label="Portrait of a dentist in a white coat"></div>
<div class="abs arrow" style="left:183px;top:1121px"><svg width="14" height="10" viewBox="0 0 14 10"><path d="M13 5H1M5 1L1 5l4 4" stroke="#333" stroke-width="1.4" fill="none"/></svg></div>
<div class="abs arrow" style="left:976px;top:1121px"><svg width="14" height="10" viewBox="0 0 14 10"><path d="M1 5h12M9 1l4 4-4 4" stroke="#333" stroke-width="1.4" fill="none"/></svg></div>
<div class="abs btn-outline" style="left:465px;top:1310px;width:270px;height:35px;line-height:32px">DOCTOR'S DETAILED INFORMATION</div>

<h2 class="abs section-title" style="top:1422px">Our Services</h2>
<div class="abs service" style="left:89px"><svg width="44" height="60" viewBox="0 0 44 60"><path d="M8 4h28v12H8zM12 16h20v8H12zM16 24h12l-2 32h-8z" fill="none" stroke="#6cb33f" stroke-width="2"/></svg><p>Dental<br>Implants</p></div>
<div class="abs service" style="left:261px"><svg width="60" height="60" viewBox="0 0 60 60"><path d="M22 14c6-4 10 0 14 0s10-4 14 2c4 8-2 18-4 26-1 6-4 12-6 6s-4-8-6-8-4 2-6 8-5 0-6-6c-2-8-6-20 0-28z" fill="none" stroke="#6cb33f" stroke-width="2"/><circle cx="8" cy="20" r="3" fill="none" stroke="#d7262d" stroke-width="2"/><circle cx="14" cy="8" r="3" fill="none" stroke="#d7262d" stroke-width="2"/></svg><p>Cosmetic<br>Dentistry</p></div>
<div class="abs service active" style="left:433px"><svg width="60" height="60" viewBox="0 0 60 60"><path d="M14 8c8-4 12 0 16 0s8-4 16 0c6 6 0 20-2 30-1 8-4 16-7 8s-4-10-7-10-4 2-7 10-6 0-7-8C14 28 8 14 14 8z" fill="none" stroke="#fff" stroke-width="2"/><path d="M12 24h36M20 18v12M40 18v12" stroke="#fff" stroke-width="2"/></svg><p style="margin-top:20px">Braces</p></div>
<div class="abs service" style="left:605px"><svg width="44" height="60" viewBox="0 0 44 60"><path d="M10 14c6-4 8 0 12 0s6-4 12 0c4 6 0 16-2 24-1 8-3 18-6 10s-2-10-4-10-2 2-4 10-5-2-6-10C10 30 6 20 10 14z" fill="none" stroke="#6cb33f" stroke-width="2"/><path d="M22 2v18M17 15l5 5 5-5" stroke="#d7262d" stroke-width="2" fill="none"/></svg><p style="margin-top:20px">Crowns</p></div>
<div class="abs service" style="left:777px"><svg width="76" height="60" viewBox="0 0 76 60"><path d="M4 20h68v18H4zM16 20v18M30 20v18M46 20v18M60 20v18" fill="none" stroke="#6cb33f" stroke-width="2"/><path d="M4 42h68" stroke="#6cb33f" stroke-width="2"/></svg><p style="margin-top:20px">Bridge</p></div>
<div class="abs service" style="left:949px"><svg width="70" height="60" viewBox="0 0 70 60"><path d="M24 20c6-4 8 0 11 0s5-4 11 0c4 6 0 14-2 22-1 6-3 10-5 6s-2-6-4-6-2 2-4 6-4 0-5-6C24 34 20 26 24 20z" fill="none" stroke="#6cb33f" stroke-width="2"/><path d="M6 52c6-10 14-12 20-8M64 52c-6-10-14-12-20-8M4 56h62" fill="none" stroke="#6cb33f" stroke-width="2"/><path d="M40 14l10-12M44 16l10-12" stroke="#d7262d" stroke-width="2"/></svg><p style="margin-top:20px">Extractions</p></div>
<div class="abs" style="left:0;top:1722px;width:1200px;text-align:center;font-size:11px;font-weight:600;color:var(--ink);text-decoration:underline">LOAD MORE</div>

<svg class="abs review-band" viewBox="0 0 1200 590" aria-hidden="true">
  <path d="M0 90 C80 40 180 5 300 5 C470 5 560 110 760 140 C950 165 1090 120 1200 60 V590 H0 Z" fill="var(--blue)"/>
</svg>
<div class="abs" style="left:0;top:1830px;width:660px;height:572px;background:linear-gradient(90deg,rgba(0,152,215,.2),rgba(0,152,215,0) 70%),radial-gradient(ellipse at 45% 55%,rgba(255,255,255,.18),rgba(255,255,255,0) 60%);border-radius:300px 0 0 0" role="img" aria-label="Photo of a smiling couple in blue tint"></div>
<h2 class="abs" style="left:120px;top:2108px;font-size:44px;color:#fff;font-weight:600">Review Widget</h2>
<div class="abs" style="left:121px;top:2168px;font-size:26px;color:#fff;font-family:'Rubik',sans-serif;font-weight:500">What Our Patients Say About Us</div>

<div class="abs widget">
  <div class="abs" style="left:0;top:18px;width:370px;text-align:center;font-size:15px;color:var(--ink)">Average Rating</div>
  <div class="abs" style="left:102px;top:48px;display:flex;gap:3px;align-items:center">
    <svg width="140" height="24" viewBox="0 0 140 24"><g fill="#f4a623"><path id="st" d="M12 1l3.4 7 7.6 1-5.5 5.3 1.3 7.6L12 18.3 5.2 21.9l1.3-7.6L1 9l7.6-1z"/><use href="#st" x="27"/><use href="#st" x="54"/><use href="#st" x="81"/></g><use href="#st" x="108" fill="#f6d48c"/></svg>
    <span style="font-size:17px;font-weight:600;color:var(--ink);margin-left:2px">4.9</span>
  </div>
  <div class="abs" style="left:132px;top:92px;display:flex;gap:8px;align-items:center;font-size:11px;font-weight:500;color:var(--ink)"><svg width="22" height="18" viewBox="0 0 22 18"><path d="M2 2h18v11H9l-5 4v-4H2z" fill="#3b8ee8"/></svg>238 Reviews</div>
  <div class="abs" style="left:26px;top:134px;width:318px;height:1px;background:#e2e5e8"></div>
  <div class="abs" style="left:47px;top:152px;width:280px;display:flex;justify-content:space-between;font-family:'Rubik',sans-serif;font-size:18px;font-weight:500;color:var(--ink)"><span>Searchly</span><span>Rateo</span><span>Circlebook</span></div>
  <svg class="abs" style="left:20px;top:325px" width="10" height="16" viewBox="0 0 10 16"><path d="M8 2L2 8l6 6" stroke="#0098d7" stroke-width="2" fill="none"/></svg>
  <svg class="abs" style="left:340px;top:325px" width="10" height="16" viewBox="0 0 10 16"><path d="M2 2l6 6-6 6" stroke="#0098d7" stroke-width="2" fill="none"/></svg>
  <div class="abs review-card">
    <div class="abs" style="left:16px;top:16px;width:52px;height:52px;border-radius:50%;background:#d9b59a" role="img" aria-label="Reviewer avatar"></div>
    <svg class="abs" style="left:82px;top:22px" width="76" height="13" viewBox="0 0 76 13"><g fill="#f4a623"><path id="ss" d="M6.5 .5l1.8 3.8 4.2.6-3 2.9.7 4.2-3.7-2-3.7 2 .7-4.2-3-2.9 4.2-.6z"/><use href="#ss" x="15"/><use href="#ss" x="30"/><use href="#ss" x="45"/><use href="#ss" x="60"/></g></svg>
    <div class="abs" style="left:82px;top:42px;font-size:15px;font-weight:600;color:var(--ink)">Lorna T.</div>
    <div class="abs" style="left:16px;top:82px;width:244px;font-size:10.5px;line-height:17.5px;color:#555">I am so happy I found Halvern Dental in Brenford. This is a long over due review since I have been seeing them for almost two years... <span style="color:var(--blue)">more</span></div>
    <div class="abs" style="left:16px;top:166px;font-size:10.5px;font-weight:500;color:#555">26 February, 2021</div>
    <div class="abs" style="left:16px;top:210px;width:238px;height:1px;background:#e0e3e6"></div>
    <div class="abs" style="left:16px;top:228px;font-size:11px;color:#777">Source:</div>
    <div class="abs" style="left:196px;top:224px;font-size:16px;font-weight:600;color:var(--ink);font-family:'Rubik',sans-serif">Rateo</div>
  </div>
</div>

<svg class="abs" style="left:0;top:2500px" width="560" height="620" viewBox="0 0 560 620" aria-hidden="true">
  <path d="M60 70 C150 15 300 0 390 20 C480 45 545 120 545 260 C545 420 480 560 360 600 C300 615 240 610 200 600 Z" fill="var(--pink)" opacity=".85"/>
</svg>
<div class="abs" style="left:0;top:2530px;width:530px;height:580px;border-radius:120px 260px 280px 40px / 180px 300px 300px 60px;background:linear-gradient(135deg,#e9d3c2,#cfa88c 55%,#f0e6e0)" role="img" aria-label="Photo of three smiling teenage girls"></div>
<h2 class="abs" style="left:603px;top:2594px;font-size:42px;line-height:48px;font-weight:600">Experience the Halvern<br>Dental Difference</h2>
<div class="abs about-text">
  <p>Your smile is our #1 priority. At Halvern Dental, we provide affordable and expert dental solutions. Whether you are looking for a family dentist or have any emergency such as needing a root canal in Brenford, we are here for you! We want to keep your teeth healthy inside and out. We don't just clean teeth and send you on your way, we want to get to know you.</p>
  <p>We accept most HMO and PPO insurances. We offer various financing options through CarePay, LendWell and In-House Plans.</p>
  <p>To constantly strive to achieve the highest level of skills and modern techniques and equipment so we can provide our patients with the best that Dentistry has to offer at our dental office in Brenford, Cedar County, CA.</p>
  <p>We provide patients with the best experience you can find in all of Southern California. We provide a comfortable and friendly atmosphere to shatter any fears you may have. We supply you with all the information on your dental health options so you can feel comfortable in the choices you make, whether it's a routine check-up or dental implants in Brenford.</p>
  <p>We are available for Emergency and Walk-ins.</p>
</div>

<div class="abs cta" role="img" aria-label="Dental office building in teal tint">
  <h2 style="margin-top:96px;font-size:40px;line-height:46px;color:#fff;font-weight:500">Committed to excellence in<br>Oral Health Care</h2>
  <div style="margin-top:8px;font-size:17px;font-family:'Rubik',sans-serif">Free Exam and X-Rays for New Patients</div>
  <div style="margin:20px auto 0;width:200px;height:42px;line-height:39px;border:2px solid var(--green);border-radius:22px;font-size:11px;font-weight:600">BOOK AN APPOINTMENT</div>
</div>

<div class="abs foot-head" style="left:162px">HALVERN DENTAL</div>
<svg class="abs" style="left:162px;top:3646px" width="10" height="14" viewBox="0 0 10 14"><path d="M5 0a5 5 0 0 1 5 5c0 4-5 9-5 9S0 9 0 5a5 5 0 0 1 5-5z" fill="var(--red)"/><circle cx="5" cy="5" r="2" fill="#fff"/></svg>
<div class="abs foot-line" style="left:183px;top:3644px;line-height:17px">48 Marlow Ave., Suite A<br>Brenford, CA 90412</div>
<svg class="abs" style="left:162px;top:3697px" width="12" height="12" viewBox="0 0 12 12"><path d="M2 0l3 3-1.5 2a7 7 0 0 0 3.5 3.5L9 7l3 3-2 2C5 12 0 7 0 2z" fill="var(--red)"/></svg>
<div class="abs foot-line" style="left:183px;top:3694px">(555) 214-7730</div>
<svg class="abs" style="left:162px;top:3722px" width="12" height="10" viewBox="0 0 12 10"><rect width="12" height="10" fill="var(--red)"/><path d="M0 0l6 5 6-5" stroke="#fff" fill="none"/></svg>
<div class="abs foot-line" style="left:183px;top:3718px">halverndental@quorvane.com</div>
<div class="abs" style="left:165px;top:3754px;font-size:12px;font-weight:600;color:var(--green);text-decoration:underline">BOOK YOUR FREE CONSULTATION</div>

<div class="abs foot-head" style="left:513px">MAP &amp; DIRECTIONS</div>
<div class="abs" style="left:513px;top:3649px;width:272px;height:141px;border:2px solid #c9cdd1;background:linear-gradient(135deg,#eceff1,#dfe4e8)" role="img" aria-label="Map showing the office location"></div>

<div class="abs foot-head" style="left:875px">OFFICE HOURS:</div>
<div class="abs hours">
  <span>Monday</span><span>10AM–7PM</span>
  <span>Tuesday</span><span>10AM–7PM</span>
  <span>Wednesday</span><span>9AM–6PM</span>
  <span>Thursday</span><span>9AM–6PM</span>
  <span>Friday</span><span>9AM–5PM</span>
  <span>Saturday</span><span>9AM–1PM</span>
</div>

<div class="abs" style="left:89px;top:3886px;width:1022px;height:1px;background:#dde1e4"></div>
<div class="abs" style="left:89px;top:3906px;font-size:12px;color:var(--ink)">All rights reserved. MyHalvernDental.com | Disclaimer &amp; Terms | Privacy Policy | Sitemap</div>
<div class="abs social" style="left:991px;top:3902px;background:#3b5998"></div>
<div class="abs social" style="left:1022px;top:3902px;background:#1da1f2"></div>
<div class="abs social" style="left:1053px;top:3902px;background:#d32323"></div>
<div class="abs social" style="left:1084px;top:3902px;background:#dd4b39"></div>
<div class="abs" style="left:1139px;top:3856px;width:32px;height:32px;border-radius:50%;background:var(--green);display:flex;align-items:center;justify-content:center"><svg width="10" height="14" viewBox="0 0 10 14"><path d="M5 13V1M1 5l4-4 4 4" stroke="#fff" stroke-width="1.6" fill="none"/></svg></div>

</body>
</html>
```